One page flyer for nonprofit focused IT company

I need a one page flyer (one side of a single 8.5x11 page) with text and graphics. The company logo is already done, and it must appear on the flyer along with other icons and graphics. The final design will be printed on heavy weight glossy paper as a handout and also distributed as a PDF.

The text is provided in an attachment, if it needs to be shortened let me know.

Industry/Entity Type

Information Technology

Requirements
Must have
• some flare (colors, icons or images)
Should not have
• While we work for nonprofits, my company is a FOR PROFIT company.

```html
<!DOCTYPE html>
<html lang="en">
<head>
<meta charset="utf-8">
<title>Meridian Systems Corporation – IT for Nonprofits</title>
<link href="https://fonts.googleapis.com/css2?family=Cabin:wght@400;500;600;700&display=swap" rel="stylesheet">
<style>
  :root{
    --brand-red:#8f1228;
    --brand-red-bright:#c8202e;
    --ink:#1c1c1c;
    --body-ink:#333;
    --dark-band:#333333;
    --paper:#ffffff;
  }
  *{box-sizing:border-box;margin:0;padding:0}
  html,body{width:974px;height:1200px;overflow:hidden;background:var(--paper)}
  body{font-family:"Cabin",sans-serif;color:var(--body-ink);position:relative}
  .flyer{position:relative;width:974px;height:1200px;overflow:hidden;background:var(--paper)}

  .hero-art{position:absolute;left:0;top:174px;width:974px;height:310px;
    background:
      linear-gradient(180deg,rgba(255,255,255,0) 0%,rgba(255,255,255,0) 58%,#ffffff 100%),
      radial-gradient(ellipse 30% 45% at 50% 62%,rgba(240,242,246,.95),rgba(240,242,246,0)),
      linear-gradient(90deg,#8d8b8e 0%,#b9b3b0 18%,#a08e86 36%,#c9c3c0 50%,#b8aaa2 66%,#b5c4dc 84%,#8eaedd 100%)}
  .header-shapes{position:absolute;left:0;top:0;width:974px;height:230px}

  .logo{position:absolute;left:42px;top:42px;width:252px;text-align:center}
  .logo-mark{display:block;width:58px;height:48px;margin:0 auto 12px;background:var(--brand-red-bright)}
  .logo-name{font-weight:600;font-size:23px;color:var(--brand-red);line-height:1.2}

  .headline{position:absolute;left:378px;top:84px;width:590px;color:#fff;
    font-weight:600;font-size:32px;line-height:41px;letter-spacing:-.2px;white-space:nowrap}

  .intro{position:absolute;left:46px;top:490px;width:883px;font-weight:700;font-size:20.2px;
    line-height:23.6px;color:var(--ink);text-align:justify;letter-spacing:-.05px}

  .item{position:absolute}
  .item h2{font-weight:600;font-size:19px;line-height:22px;color:var(--brand-red);letter-spacing:-.2px}
  .item p{font-size:14px;line-height:16.6px;text-align:justify;color:var(--body-ink)}
  .col-left .item{left:115px;width:338px}
  .col-right .item{left:569px;width:360px}
  .icon{position:absolute;width:56px;height:56px;stroke:var(--brand-red);fill:none;stroke-width:2;stroke-linecap:round;stroke-linejoin:round}

  .footer-shapes{position:absolute;left:0;top:1150px;width:974px;height:50px}
  .footer-url{position:absolute;right:47px;top:1165px;color:#fff;font-weight:600;font-size:19px}
</style>
</head>
<body>
<main class="flyer">

  <div class="hero-art" role="img" aria-label="Photo of a hand touching a screen over a world map, with cloud, laptop, globe, server and desktop icons connected in a network"></div>

  <svg class="header-shapes" viewBox="0 0 974 230" aria-hidden="true">
    <polygon points="384,48 974,48 974,174 294,174" fill="var(--brand-red)"/>
    <polygon points="0,174 294,174 267,214 0,214" fill="var(--brand-red)"/>
  </svg>

  <div class="logo">
    <span class="logo-mark"></span>
    <div class="logo-name">Meridian Systems<br>Corporation</div>
  </div>

  <h1 class="headline">An Efficient and Elegant Approach<br>to IT Solution Implementations</h1>

  <p class="intro">Meridian Systems Corporation has been supporting the Information Systems needs of nonprofits for over 50 years.&nbsp; We continually strive to bring the latest technologies and best practices to nonprofits to drive down the cost of IT while implementing systems that drive revenue.&nbsp; Our Agile approach to IT management means that we deliver working systems to every one of our clients every two weeks.</p>

  <section class="col-left">
    <svg class="icon" style="left:34px;top:626px" viewBox="0 0 58 58" aria-hidden="true">
      <circle cx="29" cy="30" r="10"/><path d="M26 26h6M26 30h6M26 34h6M29 23v14"/>
      <path d="M10 24h10M8 30h10M10 36h10M38 24h10M40 30h10M38 36h10"/>
      <path d="M44 4v12M40 8l4-4 4 4M12 44v12M8 52l4 4 4-4"/>
    </svg>
    <div class="item" style="top:622px">
      <h2>Successes<br>90% Reduction in Software<br>Development Costs</h2>
      <p>Harlan Group's National Auto Retailers Guild needed to update their core product offering; they engaged their in-house IT department who estimated the project would take 3 years at a cost of $3,000,000. NARG decided to work with Meridian Systems Corporation instead, and the product was released to production in only 9 months at one tenth of the cost, only $300,000</p>
    </div>

    <svg class="icon" style="left:36px;top:842px" viewBox="0 0 58 58" aria-hidden="true">
      <path d="M4 54h52"/><rect x="6" y="42" width="10" height="12"/><rect x="22" y="32" width="10" height="22"/><rect x="38" y="18" width="10" height="36"/>
      <path d="M8 28L26 10M16 10h10v10"/>
    </svg>
    <div class="item" style="top:835px">
      <h2>10x Increase in Membership</h2>
      <p>Greenway Paths Trust needed to move to online membership registration and contracted with Meridian Systems Corporation to build a significant online presence and engage potential members.&nbsp; Through compelling online tools and mobile applications Greenway Paths Trust has increased membership 10 fold.</p>
    </div>

    <svg class="icon" style="left:32px;top:976px" viewBox="0 0 58 58" aria-hidden="true">
      <circle cx="10" cy="10" r="7"/><path d="M17 10h8l6 4h8l10 6"/>
      <circle cx="11" cy="46" r="8"/><path d="M22 56V36h6v20M34 56V30h6v26M46 56V34h6v22"/>
    </svg>
    <div class="item" style="top:972px">
      <h2>20% Reduction in Overhead</h2>
      <p>The National Alliance for Civic Equity had antiquated systems and processes in place to manage over 500 chapters across the nation.&nbsp; Working with MSC they implemented online tools to allow communication and management between the local chapters and national headquarters.&nbsp; This eliminated much of the overhead of chapter management, reducing HR costs by 20%.</p>
    </div>
  </section>

  <section class="col-right">
    <div class="item" style="top:619px">
      <p>With a focus on non-profit websites and web based applications, MSC helps nonprofits communicate with their members and donors while maximizing online giving and engagement.</p>
    </div>

    <svg class="icon" style="left:492px;top:714px" viewBox="0 0 58 58" aria-hidden="true">
      <rect x="4" y="2" width="36" height="54" rx="4"/><path d="M12 48h14M10 10h2M14 10h2M18 10h2"/>
      <path d="M12 24h8M16 20v8M26 26l4-6 4 6z"/><path d="M38 34l6 8v12"/>
    </svg>
    <div class="item" style="top:695px">
      <h2>Mobile Applications</h2>
      <p>Meridian Systems Corporation implements mobile applications for phones and tablets to provide direct communications with members and donors enabling real-time, two way interaction.</p>
    </div>

    <svg class="icon" style="left:492px;top:810px" viewBox="0 0 58 58" aria-hidden="true">
      <circle cx="16" cy="22" r="12"/><path d="M16 16v16M12 26h8"/>
      <circle cx="40" cy="10" r="6"/><path d="M40 16v8"/>
      <rect x="30" y="38" width="10" height="16"/><path d="M8 40v14h16"/>
    </svg>
    <div class="item" style="top:797px">
      <h2>Systems Integration</h2>
      <p>Every nonprofit's IT applications are scattered and disconnected.&nbsp; Meridian Systems Corporation has decades of experience integrating these applications into a single cohesive system.</p>
    </div>

    <svg class="icon" style="left:493px;top:912px" viewBox="0 0 58 58" aria-hidden="true">
      <rect x="2" y="4" width="52" height="38"/><path d="M20 50h16M28 42v8"/>
      <path d="M8 22l6-6 6 6M10 20v6h8v-6"/><path d="M28 26V14M33 26V18M38 26V12M43 26V20"/>
      <circle cx="14" cy="34" r="4"/><path d="M26 36l6-6 6 4 8-8"/>
    </svg>
    <div class="item" style="top:902px">
      <h2>Business Intelligence and Reporting</h2>
      <p>Meridian Systems Corporation can wrestle all of an organization's data into simple executive dashboards and reports.</p>
    </div>

    <svg class="icon" style="left:493px;top:988px" viewBox="0 0 58 58" aria-hidden="true">
      <path d="M12 28a8 8 0 0 1 2-16 12 12 0 0 1 22-2 9 9 0 0 1 10 18z"/>
      <ellipse cx="30" cy="30" rx="8" ry="3"/><path d="M22 30v10c0 2 16 2 16 0V30"/>
      <path d="M10 36v12H4M48 36v12h6M30 42v12"/>
    </svg>
    <div class="item" style="top:999px">
      <h2>Cloud Migration</h2>
      <p>Reduce IT costs by migrating to the latest cloud solutions.</p>
    </div>

    <svg class="icon" style="left:492px;top:1052px" viewBox="0 0 58 58" aria-hidden="true">
      <path d="M8 34a9 9 0 0 1 4-18 14 14 0 0 1 26-4 10 10 0 0 1 10 20"/>
      <circle cx="16" cy="38" r="4"/><circle cx="29" cy="30" r="4"/><circle cx="42" cy="38" r="4"/>
      <path d="M8 52a8 8 0 0 1 16 0zM21 44a8 8 0 0 1 16 0M34 52a8 8 0 0 1 16 0z"/>
    </svg>
    <div class="item" style="top:1053px">
      <h2>Member Donor Database</h2>
      <p>Meridian Systems Corporation's GiveLedger Member / Donor CRM system is fully customized for each client meeting the unique needs of your organization.</p>
    </div>
  </section>

  <svg class="footer-shapes" viewBox="0 0 974 50" aria-hidden="true">
    <rect x="0" y="23" width="245" height="27" fill="var(--dark-band)"/>
    <polygon points="252,4 974,4 974,50 227,50" fill="var(--brand-red)"/>
  </svg>
  <div class="footer-url">www.meridiansystems.com</div>

</main>
</body>
</html>
```